Caricature Business Card for The Shade Fairy

I would like to see if you can do a caricature of a lady with shoulder length blonde curly hair wearing dark glasses and holding a measuring tape out in front of her like a walking stick, maybe in front of a window with blinds on it. I sell window coverings and I want a humorous tie in of my company name to my profession - other creative ideas will also be considered!

Industry/Entity Type

Business

Contact Information for Business Card

The Shade Fairy Doris Pemblewick"With prices you've never seen before!"Cell phone 208-409-9829Email: TheShadeFairyDoris@nextmail.example

Requirements
Must have
• A humorous tie in of the name The Shade Fairy to selling of window coverings

```html
<!DOCTYPE html>
<html lang="en">
<head>
<meta charset="utf-8">
<title>The Shade Fairy – Business Card</title>
<link rel="stylesheet" href="https://fonts.googleapis.com/css2?family=Alike&family=Arimo&display=swap">
<style>
  :root {
    --backdrop: #d6d7d8;
    --card: #ffffff;
    --navy: #2a2d62;
    --ink: #111111;
    --swoosh: #0a0a0a;
    --blind-tone: #e3e3e3;
    --on-navy: #ffffff;
  }
  html, body {
    margin: 0;
    width: 1200px;
    height: 902px;
    overflow: hidden;
    background: var(--backdrop);
  }
  .card {
    position: absolute;
    left: 50px;
    top: 137px;
    width: 1100px;
    height: 627px;
    background: var(--card);
    overflow: hidden;
    box-shadow: 0 4px 18px rgba(0,0,0,0.18);
  }
  .window-blind-art {
    position: absolute;
    left: 646px;
    top: 0;
    width: 430px;
    height: 426px;
    background: linear-gradient(180deg, var(--blind-tone), #ececec);
  }
  .card-waves {
    position: absolute;
    inset: 0;
    width: 100%;
    height: 100%;
  }
  .company-name {
    position: absolute;
    left: 50px;
    top: 60px;
    margin: 0;
    font-family: "Alike", Georgia, serif;
    font-weight: 400;
    font-size: 92px;
    line-height: 1;
    color: var(--ink);
    letter-spacing: 1px;
  }
  .tagline {
    position: absolute;
    left: 51px;
    top: 183px;
    margin: 0;
    font-family: "Arimo", Arial, sans-serif;
    font-size: 33px;
    color: var(--ink);
  }
  .contact-list {
    position: absolute;
    left: 51px;
    top: 333px;
    margin: 0;
    padding: 0;
    list-style: none;
    font-family: "Arimo", Arial, sans-serif;
    font-size: 28px;
    color: var(--ink);
  }
  .contact-item {
    display: flex;
    align-items: center;
    gap: 22px;
    height: 49px;
  }
  .contact-icon {
    width: 25px;
    height: 22px;
    flex: none;
  }
  .owner-name {
    position: absolute;
    right: 44px;
    bottom: 26px;
    margin: 0;
    font-family: "Alike", Georgia, serif;
    font-size: 42px;
    color: var(--on-navy);
    letter-spacing: 0.5px;
  }
</style>
</head>
<body>
  <section class="card">
    <div class="window-blind-art" role="img" aria-label="Faint illustration of a window blind with pull cord"></div>

    <svg class="card-waves" viewBox="0 0 800 456" preserveAspectRatio="none" aria-hidden="true">
      <path fill="var(--navy)" d="M0,343 C150,385 300,412 450,384 C600,355 700,318 800,316 L800,456 L0,456 Z"/>
      <path fill="var(--swoosh)" d="M0,326 C160,368 300,398 440,386 C590,372 700,306 800,304 L800,312 C700,318 590,384 440,392 C300,402 160,378 0,336 Z"/>
    </svg>

    <h1 class="company-name">The Shade Fairy</h1>
    <p class="tagline">With prices you've never seen before</p>

    <ul class="contact-list">
      <li class="contact-item">
        <svg class="contact-icon" viewBox="0 0 25 22" aria-hidden="true">
          <rect width="25" height="22" fill="var(--navy)"/>
          <path d="M5 9 Q12.5 3 20 9 L18 11 L15.5 9.5 L9.5 9.5 L7 11 Z" fill="#fff"/>
          <rect x="7" y="12" width="11" height="6" rx="1" fill="#fff"/>
        </svg>
        <span>208-555-0147</span>
      </li>
      <li class="contact-item">
        <svg class="contact-icon" viewBox="0 0 25 22" aria-hidden="true">
          <rect width="25" height="22" fill="var(--navy)"/>
          <rect x="5" y="6" width="15" height="10" fill="#fff"/>
          <path d="M5 6 L12.5 12 L20 6" fill="none" stroke="var(--navy)" stroke-width="1.5"/>
        </svg>
        <span>TheShadeFairyDoris@nextmail.example</span>
      </li>
    </ul>

    <p class="owner-name">Doris Pemblewick</p>
  </section>
</body>
</html>
```